Social Media Post Quote #1 - Native American Organization

- DAWNSET - must be included
- Protect your community. Protect Your Elders. Stay Vaccinated. must be included
- Attached, company Logo, campaign logos and sample flu social media image. - our audience likes BRIGHT colors.
- Must include image from the United States, representing Land/Nature from one of the following regions, Plains and Woodlands, or Southwest, or Mountains, or Coast, or Pow-wow.
- must include quote “Don’t let the flu interfere with our gatherings.” – Anonymous Tribal Member
- One image will be provided twice - incorporating campaign logos - in some fashion

```html
<!DOCTYPE html>
<html lang="en">
<head>
<meta charset="UTF-8">
<title>DAWNSET – Gatherings Quote Post</title>
<link href="https://fonts.googleapis.com/css2?family=Poppins:wght@700;800&family=Montserrat:wght@700&family=Barlow+Condensed:wght@600&family=Barlow:wght@600&display=swap" rel="stylesheet">
<style>
  :root {
    --teal: #4fa6ae;
    --teal-band: #4e97a2;
    --wine: #8c1a2b;
    --rust: #b5574f;
    --cream: #f4ede7;
    --peach: #f5bb8e;
    --plum: #5e3553;
    --plum-deep: #3e2536;
    --brown-text: #7a4c43;
    --white: #ffffff;
  }
  * { margin: 0; padding: 0; box-sizing: border-box; }
  html, body { width: 1200px; height: 1200px; overflow: hidden; background: var(--white); }
  .post {
    position: relative;
    width: 1200px;
    height: 1200px;
    overflow: hidden;
  }
  .pattern-border {
    position: absolute;
    inset: 0;
    background:
      linear-gradient(135deg, rgba(79,166,174,0.85), rgba(181,87,79,0.75) 50%, rgba(79,166,174,0.85));
  }
  .canvas-area {
    position: absolute;
    left: 59px;
    top: 59px;
    width: 1082px;
    height: 1082px;
    overflow: hidden;
    background: var(--cream);
  }
  .scene-art {
    position: absolute;
    inset: 0;
    background:
      radial-gradient(circle at 33% 72%, rgba(255,243,190,0.95) 0, rgba(255,225,160,0.6) 9%, rgba(255,200,140,0) 22%),
      linear-gradient(180deg,
        #f3eee9 0%,
        #f2e6dc 30%,
        #f6cfae 48%,
        #f7b98a 62%,
        #ef9a7a 74%,
        #9c5470 84%,
        var(--plum) 92%,
        var(--plum-deep) 100%);
  }
  .brand-block {
    position: absolute;
    left: 14px;
    top: 34px;
  }
  .campaign-name {
    display: flex;
    align-items: center;
    gap: 14px;
    font-family: "Montserrat", sans-serif;
    font-weight: 700;
    font-size: 74px;
    letter-spacing: 1px;
    color: var(--teal);
    line-height: 1;
    padding-left: 16px;
    margin-top: 22px;
  }
  .campaign-name .mark {
    width: 22px;
    height: 22px;
    background: var(--teal);
  }
  .tagline {
    margin-top: 64px;
    font-family: "Barlow", sans-serif;
    font-weight: 600;
    font-size: 11.5px;
    letter-spacing: 0.6px;
    color: var(--brown-text);
    text-transform: uppercase;
  }
  .partner-name {
    position: absolute;
    right: 38px;
    top: 150px;
    width: 190px;
    text-align: center;
    font-family: "Barlow Condensed", sans-serif;
    font-weight: 600;
    font-size: 22px;
    line-height: 1.05;
    color: var(--rust);
    text-transform: uppercase;
  }
  .quote {
    position: absolute;
    left: 0;
    right: 0;
    top: 318px;
    text-align: center;
  }
  .quote-text {
    font-family: "Poppins", sans-serif;
    font-weight: 800;
    font-size: 62px;
    line-height: 1.2;
    letter-spacing: -1.5px;
    color: var(--wine);
    paint-order: stroke fill;
    -webkit-text-stroke: 8px var(--white);
  }
  .quote-source {
    margin-top: 8px;
    font-family: "Poppins", sans-serif;
    font-weight: 800;
    font-size: 40px;
    letter-spacing: -1px;
    color: var(--teal);
    paint-order: stroke fill;
    -webkit-text-stroke: 6px var(--white);
  }
  .cta-band {
    position: absolute;
    left: 0;
    right: 0;
    top: 961px;
    height: 84px;
    background: var(--teal-band);
    display: flex;
    align-items: center;
    justify-content: center;
    font-family: "Poppins", sans-serif;
    font-weight: 700;
    font-size: 30px;
    letter-spacing: -0.3px;
    color: var(--white);
  }
  .base-strip {
    position: absolute;
    left: 0;
    right: 0;
    top: 1045px;
    bottom: 0;
    background: linear-gradient(90deg, #5a3a55, #3d2538);
  }
</style>
</head>
<body>
  <div class="post">
    <div class="pattern-border" role="img" aria-label="Woven chevron zigzag border in teal and rust"></div>

    <main class="canvas-area">
      <div class="scene-art" role="img" aria-label="Faded photo of a person with a cold holding a tissue and a warm mug, blended over an illustrated sunset behind purple and orange mountain ranges"></div>

      <header class="brand-block">
        <div class="campaign-name"><span class="mark"></span>DAWNSET</div>
        <p class="tagline">Protect your community. Protect your elders. Stay vaccinated.</p>
      </header>

      <div class="partner-name">Elder Circle Alliance</div>

      <section class="quote">
        <p class="quote-text">Don’t let the flu interfere<br>with our gatherings.”</p>
        <p class="quote-source">– Anonymous Tribal Member –</p>
      </section>

      <div class="cta-band">Learn more about getting vaccinated against COVID-19 &amp; Flu</div>
      <div class="base-strip"></div>
    </main>
  </div>
</body>
</html>
```